Real Estate "For Sale" Sign for construction company

We need a sign that we can use to hang on a post and place on the road when we sell a property. The sign will be simple and will need to mainly feature our logo (files attached), as well as the words "For Sale", and then our phone number "(555) 617 3489". The sign will hang on a post that'll look something like the attached picture.

Target Market(s)

Home buyers

Industry/Entity Type

Real Estate

Font styles to use
Serif
Sans Serif

Colors
0054AA
0677BA
7BADD7
CADEEF
E8F1F8
0094D4
00A9DD
6FCCEA
C7EBF8
E9F6FB

Requirements
Must have
• For Sale & our phone number

```html
<!DOCTYPE html>
<html lang="en">
<head>
<meta charset="utf-8">
<title>Ridgeline Homes – For Sale Sign</title>
<link href="https://fonts.googleapis.com/css2?family=Montserrat:wght@500;600;700;800&display=swap" rel="stylesheet">
<style>
  :root {
    --page-bg: #ffffff;
    --sign-bg: #e9f0f8;
    --brand-blue: #177fc4;
    --band-text: #ffffff;
  }
  html, body {
    margin: 0;
    padding: 0;
    overflow: hidden;
  }
  body {
    width: 1200px;
    height: 789px;
    background: var(--page-bg);
    position: relative;
    font-family: "Montserrat", Arial, sans-serif;
  }
  .sign {
    position: absolute;
    left: 241px;
    top: 153px;
    width: 714px;
    height: 486px;
    background: var(--sign-bg);
  }
  .sign-brand {
    position: absolute;
    left: 0;
    top: 0;
    width: 100%;
    height: 235px;
    display: flex;
    align-items: center;
    justify-content: center;
  }
  .brand-name {
    margin: 0;
    color: var(--brand-blue);
    font-weight: 600;
    font-size: 50px;
    letter-spacing: 0.5px;
  }
  .sale-band {
    position: absolute;
    left: 0;
    top: 235px;
    width: 100%;
    height: 123px;
    background: var(--brand-blue);
    display: flex;
    align-items: center;
    justify-content: center;
  }
  .sale-label {
    margin: 0;
    color: var(--band-text);
    font-weight: 800;
    font-size: 76px;
    letter-spacing: 1px;
    line-height: 1;
  }
  .sign-contact {
    position: absolute;
    left: 0;
    top: 358px;
    width: 100%;
    height: 128px;
    display: flex;
    align-items: center;
    justify-content: center;
  }
  .phone-number {
    margin: 0;
    color: var(--brand-blue);
    font-weight: 700;
    font-size: 52px;
    letter-spacing: -0.5px;
    line-height: 1;
  }
</style>
</head>
<body>
  <main class="sign">
    <header class="sign-brand">
      <p class="brand-name">Ridgeline Homes</p>
    </header>
    <section class="sale-band">
      <h1 class="sale-label">FOR SALE</h1>
    </section>
    <footer class="sign-contact">
      <p class="phone-number">(555) 617 3489</p>
    </footer>
  </main>
</body>
</html>
```